Brochure Design Project

We need a brochure design.
It is an A3 page folded into 2 A4.
The brochure is for a company at the catering services in Israel - mostly finger food trays for businesses and home events.
Most of the brochure will be like a menu (we have the photos). To every photo there will be 3-4 short sentences that describes the food presented.
The brochure will be in Hebrew language (Right to Left) - We will do all the Language stuff but need an impressive design for the brochure.
The brochure should communicate quality and pleasent feelings.

Target Market(s)

1] Businesses Events - the person that orders food for Board meetings, courses, conventions - most of the time the secretaries.
2] Home Events - like birthdays, Celebrations - most of the time the mother orders the food

Industry/Entity Type

Catering

Requirements
Must have
• We have a logo and web site (so the main colors should communicate with it).
There are 5 categories: Main dishes, Salads, Deserts, Drinks, Extras

```html
<!DOCTYPE html>
<html lang="he">
<head>
<meta charset="utf-8">
<title>Catering Menu Brochure</title>
<link href="https://fonts.googleapis.com/css2?family=Tinos:wght@700&family=Frank+Ruhl+Libre:wght@400;500&display=swap" rel="stylesheet">
<style>
  :root {
    --backdrop: #efece8;
    --paper-light: #ececec;
    --paper-mid: #d9d9d9;
    --paper-dark: #bdbdbd;
    --panel-top: #f6f6f6;
    --panel-bottom: #dcdcdc;
    --plum: #4a2535;
    --plum-soft: #6b3a4f;
    --ink: #2a2226;
    --mat: #ffffff;
    --tray: #3a2620;
  }
  * { box-sizing: border-box; margin: 0; padding: 0; }
  html, body { width: 1200px; height: 900px; overflow: hidden; }
  body { background: var(--backdrop); position: relative; }

  .spread {
    position: absolute; left: 40px; top: 54px; width: 1120px; height: 792px;
    background: radial-gradient(ellipse at 50% 35%, var(--paper-light) 0%, var(--paper-mid) 60%, var(--paper-dark) 100%);
    box-shadow: 0 6px 18px rgba(0,0,0,.25);
    overflow: hidden;
  }
  .fold {
    position: absolute; left: 548px; top: 0; width: 24px; height: 100%;
    background: linear-gradient(90deg, rgba(0,0,0,0) 0%, rgba(0,0,0,.12) 50%, rgba(0,0,0,0) 100%);
  }
  .panel {
    position: absolute; border-radius: 16px;
    background: linear-gradient(180deg, var(--panel-top), var(--panel-bottom));
    box-shadow: inset 0 0 0 1px rgba(255,255,255,.6), 0 1px 4px rgba(0,0,0,.12);
  }
  .category-title {
    position: absolute; height: 34px; padding: 0 28px;
    display: flex; align-items: center; justify-content: center;
    font-family: "Tinos", "Times New Roman", serif; font-weight: 700; font-size: 17px;
    color: #fff; background: var(--plum);
    border-radius: 40% 12px 45% 10px / 60% 20px 70% 20px;
    box-shadow: 0 0 0 3px rgba(74,37,53,.25);
  }
  .item { position: absolute; display: flex; gap: 10px; }
  .item.row { align-items: center; }
  .item.stack { flex-direction: column; align-items: center; gap: 6px; }
  .photo {
    flex: none; background: var(--mat); padding: 5px;
    box-shadow: 0 2px 5px rgba(0,0,0,.28);
  }
  .photo .fill { width: 100%; height: 100%; }
  .tray .fill { border: 4px solid var(--tray); background: linear-gradient(135deg, #c98a4a, #8e4a2c 55%, #d9b27a); }
  .tray.green .fill { background: linear-gradient(135deg, #7d9a4a, #c96a4a 55%, #e3c98a); }
  .tray.sweet .fill { background: linear-gradient(135deg, #6b3a2a, #c4864f 50%, #e9d2a8); }
  .platter .fill { border-radius: 50%; border: 3px solid #cfcfcf; background: radial-gradient(circle, #e8b85a, #b33a3a 60%, #7a2a2a); }
  .bowl .fill { border-radius: 50%; background: radial-gradient(circle, #9fbf5a 0%, #5e8a34 55%, #1f2f24 75%); }
  .bowl.red .fill { background: radial-gradient(circle, #d9603a 0%, #7fa04a 55%, #1f2f24 75%); }
  .bowl.pale .fill { background: radial-gradient(circle, #e6e2c8 0%, #b7b48a 55%, #1f2f24 75%); }
  .desc {
    font-family: "Frank Ruhl Libre", "David", serif; font-size: 11px; line-height: 1.35;
    color: var(--ink); direction: rtl; text-align: right;
  }
  .stack .desc { text-align: center; }
</style>
</head>
<body>
<main class="spread">
  <div class="fold"></div>

  <!-- Category 1 -->
  <section class="panel" style="left:30px;top:100px;width:262px;height:400px;"></section>
  <h2 class="category-title" style="left:60px;top:74px;width:210px;">Food Category 1</h2>
  <div class="item row" style="left:42px;top:120px;"><p class="desc" style="width:120px">מגש אירוח טרי ועשיר, מוכן בבוקר האירוע. מתאים ל-15 סועדים. 128 ₪ למגש</p><div class="photo tray" style="width:110px;height:62px"><div class="fill" role="img" aria-label="Photo of a finger food tray"></div></div></div>
  <div class="item row" style="left:42px;top:195px;"><p class="desc" style="width:120px">מגש אירוח טרי ועשיר, מוכן בבוקר האירוע. מתאים ל-15 סועדים. 128 ₪ למגש</p><div class="photo tray green" style="width:110px;height:62px"><div class="fill" role="img" aria-label="Photo of a tray of rolls"></div></div></div>
  <div class="item row" style="left:42px;top:270px;"><p class="desc" style="width:120px">מגש אירוח טרי ועשיר, מוכן בבוקר האירוע. מתאים ל-15 סועדים. 128 ₪ למגש</p><div class="photo tray" style="width:110px;height:62px"><div class="fill" role="img" aria-label="Photo of a tray of savoury bites"></div></div></div>
  <div class="item row" style="left:42px;top:345px;"><p class="desc" style="width:120px">מגש אירוח טרי ועשיר, מוכן בבוקר האירוע. מתאים ל-15 סועדים. 128 ₪ למגש</p><div class="photo tray" style="width:110px;height:62px"><div class="fill" role="img" aria-label="Photo of a tray of stuffed pastries"></div></div></div>
  <div class="item row" style="left:42px;top:420px;"><p class="desc" style="width:120px">מגש אירוח טרי ועשיר, מוכן בבוקר האירוע. מתאים ל-15 סועדים. 128 ₪ למגש</p><div class="photo platter" style="width:110px;height:66px"><div class="fill" role="img" aria-label="Photo of a round meat platter"></div></div></div>

  <!-- Category 3 (middle) -->
  <h2 class="category-title" style="left:450px;top:44px;width:210px;">Food Category 3</h2>
  <div class="item stack" style="left:330px;top:100px;width:200px;"><div class="photo tray sweet" style="width:120px;height:66px"><div class="fill" role="img" aria-label="Photo of a tray of macarons"></div></div><p class="desc" style="width:170px">מגש אירוח טרי ועשיר, מוכן בבוקר האירוע. מתאים ל-15 סועדים. 128 ₪ למגש</p></div>
  <div class="item stack" style="left:330px;top:240px;width:200px;"><div class="photo tray sweet" style="width:120px;height:66px"><div class="fill" role="img" aria-label="Photo of a tray of cakes"></div></div><p class="desc" style="width:170px">מגש אירוח טרי ועשיר, מוכן בבוקר האירוע. מתאים ל-15 סועדים. 128 ₪ למגש</p></div>
  <div class="item stack" style="left:330px;top:380px;width:200px;"><div class="photo tray sweet" style="width:120px;height:66px"><div class="fill" role="img" aria-label="Photo of a tray of pastries"></div></div><p class="desc" style="width:170px">מגש אירוח טרי ועשיר, מוכן בבוקר האירוע. מתאים ל-15 סועדים. 128 ₪ למגש</p></div>
  <div class="item stack" style="left:580px;top:100px;width:200px;"><div class="photo tray sweet" style="width:120px;height:66px"><div class="fill" role="img" aria-label="Photo of a tray of cookies"></div></div><p class="desc" style="width:170px">מגש אירוח טרי ועשיר, מוכן בבוקר האירוע. מתאים ל-15 סועדים. 128 ₪ למגש</p></div>
  <div class="item stack" style="left:580px;top:240px;width:200px;"><div class="photo tray sweet" style="width:120px;height:66px"><div class="fill" role="img" aria-label="Photo of a tray of brownies"></div></div><p class="desc" style="width:170px">מגש אירוח טרי ועשיר, מוכן בבוקר האירוע. מתאים ל-15 סועדים. 128 ₪ למגש</p></div>
  <div class="item stack" style="left:580px;top:380px;width:200px;"><div class="photo platter" style="width:120px;height:66px"><div class="fill" role="img" aria-label="Photo of a fruit platter"></div></div><p class="desc" style="width:170px">מגש אירוח טרי ועשיר, מוכן בבוקר האירוע. מתאים ל-15 סועדים. 128 ₪ למגש</p></div>

  <!-- Category 4 -->
  <section class="panel" style="left:810px;top:34px;width:282px;height:450px;"></section>
  <h2 class="category-title" style="left:800px;top:18px;width:190px;">Food Category 4</h2>
  <div class="item row" style="left:822px;top:58px;"><div class="photo platter" style="width:100px;height:56px"><div class="fill" role="img" aria-label="Photo of an antipasti platter"></div></div><p class="desc" style="width:150px">מגש אירוח טרי ועשיר, מוכן בבוקר האירוע. מתאים ל-15 סועדים. 128 ₪ למגש</p></div>
  <div class="item row" style="left:822px;top:128px;"><div class="photo bowl pale" style="width:100px;height:56px"><div class="fill" role="img" aria-label="Photo of a salad bowl"></div></div><p class="desc" style="width:150px">מגש אירוח טרי ועשיר, מוכן בבוקר האירוע. מתאים ל-15 סועדים. 128 ₪ למגש</p></div>
  <div class="item row" style="left:822px;top:198px;"><div class="photo bowl" style="width:100px;height:56px"><div class="fill" role="img" aria-label="Photo of a green salad bowl"></div></div><p class="desc" style="width:150px">מגש אירוח טרי ועשיר, מוכן בבוקר האירוע. מתאים ל-15 סועדים. 128 ₪ למגש</p></div>
  <div class="item row" style="left:822px;top:268px;"><div class="photo bowl" style="width:100px;height:56px"><div class="fill" role="img" aria-label="Photo of a leafy salad bowl"></div></div><p class="desc" style="width:150px">מגש אירוח טרי ועשיר, מוכן בבוקר האירוע. מתאים ל-15 סועדים. 128 ₪ למגש</p></div>
  <div class="item row" style="left:822px;top:338px;"><div class="photo bowl red" style="width:100px;height:56px"><div class="fill" role="img" aria-label="Photo of a tomato salad bowl"></div></div><p class="desc" style="width:150px">מגש אירוח טרי ועשיר, מוכן בבוקר האירוע. מתאים ל-15 סועדים. 128 ₪ למגש</p></div>
  <div class="item row" style="left:822px;top:408px;"><div class="photo bowl pale" style="width:100px;height:56px"><div class="fill" role="img" aria-label="Photo of a pasta salad bowl"></div></div><p class="desc" style="width:150px">מגש אירוח טרי ועשיר, מוכן בבוקר האירוע. מתאים ל-15 סועדים. 128 ₪ למגש</p></div>

  <!-- Category 3 (bottom band) -->
  <section class="panel" style="left:30px;top:530px;width:1062px;height:242px;"></section>
  <h2 class="category-title" style="left:455px;top:514px;width:210px;">Food Category 3</h2>
  <div class="item stack" style="left:40px;top:572px;width:128px;"><div class="photo tray sweet" style="width:110px;height:62px"><div class="fill" role="img" aria-label="Photo of a tray of petit fours"></div></div><p class="desc" style="width:124px">מגש אירוח טרי ועשיר, מוכן בבוקר האירוע. מתאים ל-15 סועדים. 128 ₪ למגש</p></div>
  <div class="item stack" style="left:171px;top:572px;width:128px;"><div class="photo tray green" style="width:110px;height:62px"><div class="fill" role="img" aria-label="Photo of a tray of canapés"></div></div><p class="desc" style="width:124px">מגש אירוח טרי ועשיר, מוכן בבוקר האירוע. מתאים ל-15 סועדים. 128 ₪ למגש</p></div>
  <div class="item stack" style="left:302px;top:572px;width:128px;"><div class="photo tray" style="width:110px;height:62px"><div class="fill" role="img" aria-label="Photo of a tray of mini sandwiches"></div></div><p class="desc" style="width:124px">מגש אירוח טרי ועשיר, מוכן בבוקר האירוע. מתאים ל-15 סועדים. 128 ₪ למגש</p></div>
  <div class="item stack" style="left:433px;top:572px;width:128px;"><div class="photo tray" style="width:110px;height:62px"><div class="fill" role="img" aria-label="Photo of a tray of quiches"></div></div><p class="desc" style="width:124px">מגש אירוח טרי ועשיר, מוכן בבוקר האירוע. מתאים ל-15 סועדים. 128 ₪ למגש</p></div>
  <div class="item stack" style="left:564px;top:572px;width:128px;"><div class="photo tray green" style="width:110px;height:62px"><div class="fill" role="img" aria-label="Photo of a tray of bite-size snacks"></div></div><p class="desc" style="width:124px">מגש אירוח טרי ועשיר, מוכן בבוקר האירוע. מתאים ל-15 סועדים. 128 ₪ למגש</p></div>
  <div class="item stack" style="left:695px;top:572px;width:128px;"><div class="photo tray" style="width:110px;height:62px"><div class="fill" role="img" aria-label="Photo of a tray of wraps"></div></div><p class="desc" style="width:124px">מגש אירוח טרי ועשיר, מוכן בבוקר האירוע. מתאים ל-15 סועדים. 128 ₪ למגש</p></div>
  <div class="item stack" style="left:826px;top:572px;width:128px;"><div class="photo tray sweet" style="width:110px;height:62px"><div class="fill" role="img" aria-label="Photo of a tray of triangle sandwiches"></div></div><p class="desc" style="width:124px">מגש אירוח טרי ועשיר, מוכן בבוקר האירוע. מתאים ל-15 סועדים. 128 ₪ למגש</p></div>
  <div class="item stack" style="left:957px;top:572px;width:128px;"><div class="photo tray sweet" style="width:110px;height:62px"><div class="fill" role="img" aria-label="Photo of a tray of baked rolls"></div></div><p class="desc" style="width:124px">מגש אירוח טרי ועשיר, מוכן בבוקר האירוע. מתאים ל-15 סועדים. 128 ₪ למגש</p></div>
</main>
</body>
</html>
```